Audio-Visual & Video Communications Business Requires a Cutting-edge Business Card Design

LinkVessel is a new Audio-Visual & Video Communications company in Cape Town, South Africa that is looking for a cutting-edge business card design. We sell these products to the Corporate, Education & Hospitality markets and will also host an Online Shop for companies and individuals to purchase our products online.

We are already using the following two colours in our logo and draft website. Please incorporate these colours into the design. Please note that our website is still in the design stage if you need to visit it. Green #a0ce4e & Dark Grey #333333.
Updates

Hi,

Please note that I have uploaded our logo in an .eps format.

Target Market(s)

Corporate Companies, Education Institutions & Hospitality Markets

Industry/Entity Type

Business

Requirements
Nice to have
• It would be great if you could incorporate the services that we offer.

1. Consultation & Design
2. Project Management
3. Supply & Installation
4. Onsite Support Personal
5. Online Shop

```html
<!DOCTYPE html>
<html lang="en">
<head>
<meta charset="utf-8">
<title>LinkVessel Business Card</title>
<link href="https://fonts.googleapis.com/css2?family=Open+Sans:wght@600&family=Arimo:wght@400;700&display=swap" rel="stylesheet">
<style>
  :root {
    --green: #a0ce4e;
    --green-light: #b8dc78;
    --grey: #333333;
    --grey-mid: #555555;
    --white: #ffffff;
    --bg: #e9e9e6;
  }
  * { box-sizing: border-box; margin: 0; padding: 0; }
  html, body { width: 1200px; height: 960px; overflow: hidden; background: var(--bg); }
  body { position: relative; font-family: "Arimo", Arial, sans-serif; }

  .card {
    position: absolute;
    width: 680px;
    height: 390px;
    overflow: hidden;
    box-shadow: 0 6px 18px rgba(0,0,0,0.18);
  }

  /* Front */
  .card-front { left: 70px; top: 60px; background: var(--green); }
  .front-top {
    position: absolute; left: 0; top: 0; width: 100%; height: 205px;
    background: var(--white);
    display: flex; align-items: center; justify-content: center; gap: 18px;
  }
  .brand-dot { width: 46px; height: 46px; border-radius: 50%; background: var(--green); }
  .brand-name {
    font-family: "Open Sans", Arial, sans-serif; font-weight: 600;
    font-size: 48px; color: var(--green); letter-spacing: -0.5px;
  }
  .front-band { position: absolute; left: 0; top: 205px; width: 100%; height: 10px; background: var(--grey); }
  .front-pointer { position: absolute; left: 88px; top: 214px; }
  .front-divider { position: absolute; left: 370px; top: 228px; width: 1px; height: 150px; background: rgba(255,255,255,0.35); }

  .person { position: absolute; left: 38px; top: 265px; }
  .person-name { font-family: "Arimo", Arial, sans-serif; font-weight: 700; font-size: 25px; color: var(--grey); }
  .person-role { font-size: 19px; color: var(--white); margin-top: 4px; }

  .contact { position: absolute; left: 392px; top: 232px; color: var(--grey); font-size: 15px; line-height: 20px; }
  .contact-address { margin-bottom: 14px; }
  .contact-line { display: flex; align-items: center; gap: 8px; margin-bottom: 3px; }
  .contact-icon { width: 18px; height: 18px; flex: none; }

  /* Back */
  .card-back {
    left: 450px; top: 510px;
    background: linear-gradient(100deg, var(--green) 0%, var(--green) 55%, var(--green-light) 72%, var(--green) 90%);
  }
  .services { position: absolute; left: 48px; top: 92px; color: #111; }
  .services-title { font-weight: 700; font-size: 15px; letter-spacing: 1px; margin-bottom: 16px; }
  .services-list { list-style: none; font-size: 15px; letter-spacing: 0.6px; line-height: 19px; }
  .services-list li::before { content: "\25AA"; margin-right: 10px; font-size: 11px; }
  .back-mark {
    position: absolute; left: 440px; top: 30px; width: 310px; height: 310px;
    border-radius: 50%; background: var(--grey-mid); opacity: 0.85;
  }
</style>
</head>
<body>

<section class="card card-front" aria-label="Business card front">
  <div class="front-top">
    <span class="brand-dot"></span>
    <span class="brand-name">LinkVessel</span>
  </div>
  <div class="front-band"></div>
  <svg class="front-pointer" width="40" height="26" viewBox="0 0 40 26"><polygon points="0,0 40,0 20,26" fill="#333333"/></svg>
  <div class="front-divider"></div>

  <div class="person">
    <div class="person-name">DANIEL MOREAU</div>
    <div class="person-role">Founder</div>
  </div>

  <div class="contact">
    <p class="contact-address">The Harbourview, Marina Park,<br>Cape Town, South Africa,<br>7400</p>
    <p class="contact-line">
      <svg class="contact-icon" viewBox="0 0 18 18"><rect x="1" y="1" width="16" height="16" rx="2" fill="none" stroke="#fff" stroke-width="1.5"/><rect x="4" y="6" width="10" height="7" fill="none" stroke="#fff" stroke-width="1.2"/><polyline points="4,6 9,10 14,6" fill="none" stroke="#fff" stroke-width="1.2"/></svg>
      info@linkvessel.co.za
    </p>
    <p class="contact-line">
      <svg class="contact-icon" viewBox="0 0 18 18"><rect x="1" y="1" width="16" height="16" rx="2" fill="none" stroke="#fff" stroke-width="1.5"/><path d="M6 4 L8 7 L7 8 Q8 10 10 11 L11 10 L14 12 L13 14 Q8 14 5 9 Q4 6 6 4 Z" fill="#fff"/></svg>
      +27 21 555-0142
    </p>
    <p class="contact-line">
      <svg class="contact-icon" viewBox="0 0 18 18"><rect x="1" y="1" width="16" height="16" rx="2" fill="none" stroke="#fff" stroke-width="1.5"/><circle cx="9" cy="9" r="4.5" fill="none" stroke="#fff" stroke-width="1.2"/><line x1="4.5" y1="9" x2="13.5" y2="9" stroke="#fff" stroke-width="1"/><ellipse cx="9" cy="9" rx="2" ry="4.5" fill="none" stroke="#fff" stroke-width="1"/></svg>
      www.linkvessel.co.za
    </p>
  </div>
</section>

<section class="card card-back" aria-label="Business card back">
  <div class="services">
    <h2 class="services-title">SERVICES:</h2>
    <ul class="services-list">
      <li>Consultation &amp; Design</li>
      <li>Project Management</li>
      <li>Supply &amp; Installation</li>
      <li>Onsite Support Personal</li>
      <li>Online Shop</li>
    </ul>
  </div>
  <div class="back-mark"></div>
</section>

</body>
</html>
```